Update of unique sports email website.

Hello.
I would like you to update a ol' archived website of mine. Bring it back to life with updated html5 or wordpress with plugins. I will provide the wordpress plugins by downloading from wordpress.org. It has 5-6 pages. Will need to update some stock sports photos.
It will be hosted on a vps server with linux and fantastico and softicious installed.
The website caters to the middle, junior, and high schools in america that has a mascot for their sports teams. The website will provide vanity email addresses that will be forwarded to their home/work/school email account. We will need a form that confirms valid email information on a form, send a confirmation page to the new clients email address that is given , they click that to confirm their enrollment. A paypal link to be installed.
I can and will provide the previous attempts of this website for any guidance and reflection to the new updated version. Other websites that are similar, or we like the design or copy : www.Brightpostal.net for frontpage colors and whitespace.
Target Market(s)
this updated website will have clicks from all over the world. the paying customer will be from mostly the united states. Sports audience. Middle schoolers, high schoolers, parents, coaches, teachers, students, administrators who all want a highly desirable sports email address of their favorite team, or local high school .
Talvix Marketing has identified and acquired the most popular sports mascots in America's most popular high school sports. We want to offer these two-worded domains to the sports amateur market. No professional teams. Strictly high schools and young adults.
Industry/Entity Type
School
Requirements
Must have
- easy to read, easy to look at, easy on the eyes. Lots of white space. A few colors . Standard black text/fonts.
A paypal.com link to accept immediate payments. Then a confirmation email sent to him and us(talvix, inc) indicating the quick payment and start processing his email request by hand. A human will always look/check/verify the email address request.
Professional look. Classy look. Fast loading.
html5 complied.
Somekind of interesting header.
Need to handle the sports: Baseball, basketball, lacrosse(lax), football, volleyball, softball, track, and soccer.
Should not have
- sloppy text and pages.
ugly colors and combinations.
Lots of questions.

```html
<!DOCTYPE html>
<html lang="en">
<head>
<meta charset="utf-8">
<title>TeamVaultMail.com</title>
<link rel="stylesheet" href="https://fonts.googleapis.com/css2?family=Arimo:wght@400;700&family=Shadows+Into+Light&display=swap">
<style>
:root{
  --ink:#000;
  --text:#1e1e1e;
  --muted:#444;
  --link:#0a4fc4;
  --brand-blue:#0a5cc8;
  --band-top:#0b63d2;
  --band-bottom:#0752b8;
  --field-border:#b9b9b9;
  --orange-top:#ffb12b;
  --orange-bottom:#f08400;
  --baseball:#1b86e8;
  --basketball:#8a4f12;
  --football:#ee4a2c;
  --golf:#7ccc17;
  --lacrosse:#f5d21a;
  --soccer:#e8479c;
  --track:#ee7a24;
  --volleyball:#9b34f0;
  --others:#111;
}
*{box-sizing:border-box;margin:0;padding:0}
html,body{width:1200px;height:922px;overflow:hidden;background:#fff}
body{position:relative;font-family:"Arimo",Arial,sans-serif;color:var(--text)}

.account-prompt{position:absolute;top:15px;left:883px;font-size:13.5px;color:var(--muted)}
.account-prompt a{color:var(--link);margin-left:16px}

.site-name{position:absolute;left:40px;top:46px;font-size:40px;font-weight:700;color:var(--ink);letter-spacing:-.5px}

.login{position:absolute;top:52px;left:716px;display:flex;gap:8px}
.field{height:35px;border:1px solid var(--field-border);border-radius:3px;background:#fff;font:14px "Arimo",sans-serif;color:#666;padding:0 10px;display:flex;align-items:center}
.login .field{width:175px}
.login-btn{width:76px;height:35px;border:1px solid #bbb;border-radius:3px;background:linear-gradient(#fafafa,#dcdcdc);font:700 14px "Arimo",sans-serif;color:#333;display:flex;align-items:center;justify-content:center}

.main-nav{position:absolute;top:104px;left:538px;display:flex;gap:4px}
.main-nav a{height:37px;padding:0 14px;border:2px solid #000;border-bottom:none;border-radius:7px 7px 0 0;background:linear-gradient(#777,#111 70%);color:#fff;font-size:16.5px;display:flex;align-items:center;text-decoration:none}
.main-nav a.active{background:#fff;color:#000;height:38px;position:relative;z-index:2}

.panel{position:absolute;left:36px;top:140px;width:1137px;height:654px;border:2px solid #000;border-radius:14px;overflow:hidden;background:#fff}
.welcome{position:absolute;left:38px;top:30px;font-size:35px;font-weight:700;color:var(--brand-blue)}
.intro{position:absolute;left:38px;top:82px;width:1060px;font-size:19px;font-weight:700;line-height:33.6px;color:var(--text);letter-spacing:.2px}
.intro a{color:var(--link)}

.athletes{position:absolute;left:0;top:270px;width:100%;height:192px;display:flex;gap:2px}
.athletes div{flex:1}

.sport-tabs{position:absolute;left:0;top:462px;width:100%;height:36px;display:flex;gap:2px}
.sport-tabs span{flex:1;border-radius:6px 6px 0 0;color:#fff;font-size:15px;font-weight:700;display:flex;align-items:center;justify-content:center;letter-spacing:.3px;border:1px solid rgba(0,0,0,.25);border-bottom:none}

.search-band{position:absolute;left:0;top:496px;width:100%;height:158px;background:linear-gradient(var(--band-top),var(--band-bottom))}
.search-title{position:absolute;left:0;width:100%;top:34px;padding-left:56px;text-align:center;font-size:19px;font-weight:700;color:#fff}
.start-here{position:absolute;left:58px;top:68px;font-family:"Shadows Into Light",cursive;font-size:36px;color:#fff}
.search-form{position:absolute;left:262px;top:82px;display:flex;align-items:center}
.search-form .field{height:35px;width:256px;font-size:16px;font-weight:700;color:#555}
.at{width:44px;text-align:center;color:#fff;font-size:24px;font-weight:700}
.go-btn{margin-left:9px;width:190px;height:35px;border-radius:3px;background:linear-gradient(var(--orange-top),var(--orange-bottom));color:#fff;font-size:16.5px;font-weight:700;display:flex;align-items:center;justify-content:center;border:1px solid #d77400}
.band-arrow{position:absolute}

.footer-nav{position:absolute;top:822px;left:0;width:1200px;text-align:center;font-size:14.5px;font-weight:700}
.footer-nav a{color:#000;text-decoration:none;margin:0 14px}
.footer-nav .sep{color:#000;font-weight:400}
.legal{position:absolute;top:854px;left:0;width:1200px;text-align:center;font-size:12.5px;color:#111}
</style>
</head>
<body>
<p class="account-prompt">Don't have an account? <a href="#">Register now!</a></p>
<div class="site-name">teamvaultmail.com</div>

<form class="login">
  <div class="field">Username</div>
  <div class="field">Password</div>
  <div class="login-btn">Login</div>
</form>

<nav class="main-nav">
  <a class="active" href="#">Home</a>
  <a href="#">About Us</a>
  <a href="#">Mascots</a>
  <a href="#">Merchandise</a>
  <a href="#">FAQ</a>
  <a href="#">Contact Us</a>
</nav>

<main class="panel">
  <h1 class="welcome">Welcome to TeamVaultMail.com</h1>
  <p class="intro">The Internet's Largest Purveyor of High Schools, Colleges, and Universities Nicknames and Team Mascots for Email and Team Websites. View our Serious <a href="#">Collection</a> of America's Most Famous Nicknames and Team Mascots. Each Will Be Available For All Your Team Email Needs.</p>

  <div class="athletes">
    <div role="img" aria-label="Blue silhouette of a baseball pitcher" style="background:linear-gradient(#fff 10%,#a9d2f7)"></div>
    <div role="img" aria-label="Brown silhouette of a basketball player dribbling" style="background:linear-gradient(#fff 10%,#d2b595)"></div>
    <div role="img" aria-label="Red silhouette of a football player" style="background:linear-gradient(#fff 10%,#f6b0a2)"></div>
    <div role="img" aria-label="Green silhouette of a golfer swinging" style="background:linear-gradient(#fff 10%,#c8ea9c)"></div>
    <div role="img" aria-label="Yellow silhouette of a lacrosse player" style="background:linear-gradient(#fff 10%,#faec9a)"></div>
    <div role="img" aria-label="Pink silhouette of a soccer player" style="background:linear-gradient(#fff 10%,#f5b2d5)"></div>
    <div role="img" aria-label="Orange silhouette of a sprinter" style="background:linear-gradient(#fff 10%,#f7c6a0)"></div>
    <div role="img" aria-label="Purple silhouette of a volleyball spiker" style="background:linear-gradient(#fff 10%,#d5aaf8)"></div>
    <div role="img" aria-label="Black silhouettes of wrestlers and a tennis player" style="background:linear-gradient(#fff 10%,#b8b8b8)"></div>
  </div>

  <div class="sport-tabs">
    <span style="background:var(--baseball)">BASEBALL</span>
    <span style="background:var(--basketball)">BASKETBALL</span>
    <span style="background:var(--football)">FOOTBALL</span>
    <span style="background:var(--golf)">GOLF</span>
    <span style="background:var(--lacrosse)">LACROSSE</span>
    <span style="background:var(--soccer)">SOCCER</span>
    <span style="background:var(--track)">TRACK</span>
    <span style="background:var(--volleyball)">VOLLEYBALL</span>
    <span style="background:var(--others)">OTHERS</span>
  </div>

  <section class="search-band">
    <p class="search-title">Enter your high school team name to search for your new unique address</p>
    <span class="start-here">start here</span>
    <svg class="band-arrow" style="left:82px;top:112px" width="180" height="40" viewBox="0 0 180 40" fill="none" stroke="#fff" stroke-width="2.5" stroke-linecap="round">
      <path d="M4 32 Q90 36 170 14"/><path d="M156 10 L171 13 L163 26"/>
    </svg>
    <form class="search-form">
      <div class="field">Username</div>
      <span class="at">@</span>
      <div class="field">High School Team</div>
      <div class="go-btn">GET MY NEW EMAIL</div>
    </form>
    <svg class="band-arrow" style="left:990px;top:38px" width="110" height="80" viewBox="0 0 110 80" fill="none" stroke="#fff" stroke-width="2.5" stroke-linecap="round">
      <path d="M4 6 Q100 4 92 42 Q86 60 66 72"/><path d="M66 60 L65 73 L79 72"/>
    </svg>
  </section>
</main>

<nav class="footer-nav">
  <a href="#">Home</a><span class="sep">|</span>
  <a href="#">Mascots</a><span class="sep">|</span>
  <a href="#">About Us</a><span class="sep">|</span>
  <a href="#">Merchandise</a><span class="sep">|</span>
  <a href="#">FAQ</a><span class="sep">|</span>
  <a href="#">Contact Us</a>
</nav>
<p class="legal">This Sports Mail Service Is Not Sponsored or Owned by Any professional , collegiate, or high school organization. A Talvix Marketing venture.</p>
</body>
</html>
```